Donor Thank You Card – Evelyn’s Harbor Pregnancy & Family Support

Project Overview:
We are seeking a heartfelt, beautifully designed thank-you card for our nonprofit, Evelyn’s Harbor Pregnancy & Family Support. This card will be sent to donors as a tangible expression of gratitude from Evelyn’s Family.

The design should feel warm, personal, and meaningful—something a recipient would want to keep.

About the Organization
Evelyn’s Harbor Pregnancy & Family Support exists to support families navigating complicated pregnancies, prolonged hospital stays, and loss.
The organization was created in honor of Evelyn, and everything we do is centered around providing comfort, connection, and a “web of care” during life’s most difficult moments.

Design Objective
Create a thank-you card that conveys:
-Deep gratitude
-Compassion and warmth
-A sense of connection and care
Subtle remembrance and hope
-This should feel personal and heartfelt—not corporate or transactional.

Color Palette: Neutrals (cream, soft beige, warm white)
Soft pastels (blush, sage, muted gold, light blue)
Avoid anything too bold or high contrast

Visual Elements:
Subtle “web” motif (very delicate—not literal or harsh)
Soft sunlight / glow elements (“little sunshine” theme)
Organic textures (linen, paper grain, watercolor feel)
Minimalist line illustrations

Card Format
Standard folded card (5x7 preferred)
Front + inside spread
Front of Card (Minimal + Elegant)

Option 1:
Evelyn’s Harbor logo
Short phrase:
“With gratitude”

Option 2:
Logo + subtle design element (sunlight/web texture)
No text or very minimal text

Inside of Card (Main Message)
Include this message:
Because of you, a family will feel supported during one of the most difficult moments of their lives.

Your generosity helps us provide comfort, care, and connection to families navigating complicated pregnancies, prolonged hospital stays, and loss.

From the bottom of our hearts, thank you for being part of this web of support.

With gratitude,
Evelyn’s Family

Back of Card:
Logo: (See attachments)
Website URL: www.evelynsharborsupport.org
Small tagline: “Woven with care, held with hope, and touched by a little sunshine.”

Let me know if you need any other variations of the logo.

Thank you!

```html
<!DOCTYPE html>
<html lang="en">
<head>
<meta charset="utf-8">
<title>Evelyn’s Harbor – Donor Thank You Card</title>
<link rel="stylesheet" href="https://fonts.googleapis.com/css2?family=Montserrat:wght@400;500&family=Playfair+Display:ital,wght@0,400;0,500;1,400;1,700&family=Mrs+Saint+Delafield&display=swap">
<style>
  :root {
    --board: #bfa090;
    --board-title: #ffffff;
    --paper-blush: #f8eeee;
    --paper-white: #ffffff;
    --paper-cream: #f9f4f1;
    --gold: #b8925c;
    --lavender: #9c7fb3;
    --sage: #6f7e6c;
    --plum: #7a3557;
    --ink: #2a2226;
    --grey-ink: #5b5458;
    --wash-lilac: #d8c8e6;
    --web-faint: #f2e6d6;
  }
  * { box-sizing: border-box; margin: 0; padding: 0; }
  html, body { width: 853px; height: 1200px; overflow: hidden; }
  body { background: var(--board); position: relative; font-family: "Playfair Display", serif; }

  .section-title {
    position: absolute; left: 0; width: 853px; text-align: center;
    font-family: "Montserrat", sans-serif; font-weight: 400;
    color: var(--board-title); font-size: 20px; letter-spacing: 1px;
  }
  .section-title--outer { top: 44px; }
  .section-title--inner { top: 625px; }

  .card {
    position: absolute; left: 69px; width: 715px; height: 501px;
    box-shadow: 0 3px 8px rgba(80, 50, 40, 0.25);
    overflow: hidden;
  }
  .card--outer { top: 79px; display: flex; }
  .card--inner { top: 663px; background: var(--paper-cream); }

  /* Front panel */
  .front {
    position: relative; width: 357px; height: 100%;
    background: radial-gradient(ellipse at 50% 45%, #fdf7f6 0%, var(--paper-blush) 80%);
  }
  .front__frame {
    position: absolute; left: 19px; top: 11px; width: 322px; height: 478px;
    border: 1px solid var(--gold);
  }
  .front__corner {
    position: absolute; width: 56px; height: 56px;
    background: radial-gradient(circle at var(--cx) var(--cy), rgba(184,146,92,0.28), rgba(184,146,92,0) 70%);
  }
  .front__corner--tl { left: 19px; top: 11px; --cx: 0% ; --cy: 0%; }
  .front__corner--tr { right: 16px; top: 11px; --cx: 100%; --cy: 0%; }
  .front__corner--bl { left: 19px; bottom: 12px; --cx: 0%; --cy: 100%; }
  .front__corner--br { right: 16px; bottom: 12px; --cx: 100%; --cy: 100%; }

  .front__name {
    position: absolute; left: 0; width: 100%; top: 214px; text-align: center;
    color: var(--lavender); font-size: 29px; font-weight: 400; line-height: 1.1;
  }
  .front__sub {
    position: absolute; left: 0; width: 100%; top: 256px; text-align: center;
    color: var(--lavender); font-size: 14px; letter-spacing: 1.5px;
  }
  .front__phrase {
    position: absolute; left: 0; width: 100%; top: 290px; text-align: center;
    font-family: "Mrs Saint Delafield", cursive; color: var(--gold);
    font-size: 40px; line-height: 1;
  }

  /* Back panel */
  .back { position: relative; flex: 1; background: var(--paper-white); }
  .back__brand {
    position: absolute; left: 0; width: 100%; top: 342px;
    display: flex; align-items: center; justify-content: center; gap: 8px;
  }
  .back__dot { width: 9px; height: 9px; border-radius: 50%; background: var(--lavender); }
  .back__name { color: var(--lavender); font-size: 19px; line-height: 1; }
  .back__sub {
    position: absolute; left: 0; width: 100%; top: 366px; text-align: center;
    color: var(--lavender); font-size: 9px; letter-spacing: 1px;
  }
  .back__tagline {
    position: absolute; left: 0; width: 100%; top: 401px; text-align: center;
    color: var(--plum); font-style: italic; font-weight: 700; font-size: 7.5px;
  }
  .back__url {
    position: absolute; left: 0; width: 100%; top: 462px; text-align: center;
    color: var(--grey-ink); font-size: 10px; font-weight: 500;
  }

  /* Inner spread */
  .inner__art {
    position: absolute; left: 0; top: 0; width: 404px; height: 450px;
    background:
      radial-gradient(ellipse at 25% 45%, #b8485e 0%, rgba(184,72,94,0) 45%),
      radial-gradient(ellipse at 70% 45%, #7b4fb0 0%, rgba(123,79,176,0) 55%),
      linear-gradient(180deg, rgba(249,244,241,0) 0%, rgba(249,244,241,0) 80%, var(--paper-cream) 100%);
  }
  .inner__web {
    position: absolute; right: 0; top: 0; width: 140px; height: 230px;
    background: radial-gradient(ellipse at 100% 20%, var(--web-faint) 0%, rgba(242,230,214,0) 70%);
  }
  .inner__wash {
    position: absolute; left: 0; bottom: 0; width: 100%; height: 90px;
    background: linear-gradient(180deg, rgba(216,200,230,0) 0%, var(--wash-lilac) 65%, #cdb8df 100%);
  }
  .message {
    position: absolute; left: 416px; width: 240px; top: 75px;
    text-align: center; font-style: italic; color: var(--ink);
    font-size: 11.6px; line-height: 21px;
  }
  .message p + p { margin-top: 21px; }
  .message__sign { font-weight: 700; }
</style>
</head>
<body>
  <h2 class="section-title section-title--outer">OUTER DESIGN</h2>

  <section class="card card--outer">
    <div class="front">
      <div class="front__frame"></div>
      <div class="front__corner front__corner--tl" role="img" aria-label="Fine gold cobweb corner ornament"></div>
      <div class="front__corner front__corner--tr" role="img" aria-label="Fine gold cobweb corner ornament"></div>
      <div class="front__corner front__corner--bl" role="img" aria-label="Fine gold cobweb corner ornament"></div>
      <div class="front__corner front__corner--br" role="img" aria-label="Fine gold cobweb corner ornament"></div>
      <div class="front__name">Evelyn’s Harbor</div>
      <div class="front__sub">Pregnancy &amp; Family Support</div>
      <div class="front__phrase">With gratitude</div>
    </div>
    <div class="back">
      <div class="back__brand">
        <span class="back__dot"></span>
        <span class="back__name">Evelyn’s Harbor</span>
      </div>
      <div class="back__sub">Pregnancy &amp; Family Support</div>
      <p class="back__tagline">“Woven with care, held with hope, and touched by a little sunshine.”</p>
      <p class="back__url">www.evelynsharborsupport.org</p>
    </div>
  </section>

  <h2 class="section-title section-title--inner">INNER SPREAD DESIGN</h2>

  <section class="card card--inner">
    <div class="inner__art" role="img" aria-label="Watercolour butterfly with a rose-red wing and a wing of purple flowers woven through a delicate web"></div>
    <div class="inner__web" role="img" aria-label="Faint cream cobweb pattern"></div>
    <div class="inner__wash" role="img" aria-label="Soft lilac watercolour wash with small butterflies"></div>
    <div class="message">
      <p>Because of you, a family will feel supported during one of the most difficult moments of their lives.</p>
      <p>Your generosity helps us provide comfort, care, and connection to families navigating complicated pregnancies, prolonged hospital stays, and loss.</p>
      <p>From the bottom of our hearts, thank you for being part of this web of support.</p>
      <p>With gratitude,<br><span class="message__sign">Evelyn’s Family</span></p>
    </div>
  </section>
</body>
</html>
```